KVR Noblesville Sign

I need to have a sign designed for a new self-storage facility we are going to be opening. The sign will be 4'W X 8'H.

Industry/Entity Type

Self Storage

Requirements
Must have
• Harbor Locker Yard logo at the top of the sign, under the logo I want the rendering.
• I also must have this information on the sign:
• 1. OPENING FALL 2016
• 2. Your premier self-storage facility.
• 3. www.harborlockeryard.example

```html
<!DOCTYPE html>
<html lang="en">
<head>
<meta charset="utf-8">
<title>Harbor Locker Yard – Opening Sign</title>
<link href="https://fonts.googleapis.com/css2?family=Anton&family=Oswald:wght@600&family=Roboto+Condensed:wght@700&display=swap" rel="stylesheet">
<style>
  :root {
    --backdrop: #e9e7e2;
    --panel: #3b3b3b;
    --sign-yellow: #f5ec12;
    --sign-red: #e01f26;
    --sign-green: #1f9a3a;
  }
  html, body {
    margin: 0;
    padding: 0;
    width: 1200px;
    height: 692px;
    overflow: hidden;
    background: var(--backdrop);
  }
  .canvas {
    position: relative;
    width: 1200px;
    height: 692px;
  }
  .sign {
    position: absolute;
    left: 450px;
    top: 46px;
    width: 300px;
    height: 600px;
    background: var(--panel);
    box-shadow: 0 6px 18px rgba(0,0,0,0.25);
    text-align: center;
  }
  .sign__opening {
    position: absolute;
    top: 18px;
    left: 0;
    right: 0;
    margin: 0;
    font-family: "Oswald", sans-serif;
    font-weight: 600;
    font-size: 31px;
    letter-spacing: 0.5px;
    color: var(--sign-yellow);
  }
  .sign__brand {
    position: absolute;
    top: 84px;
    left: 22px;
    right: 22px;
    height: 256px;
    display: flex;
    flex-direction: column;
    align-items: center;
    justify-content: center;
    gap: 14px;
  }
  .sign__brand-mark {
    width: 26px;
    height: 26px;
    background: var(--sign-yellow);
  }
  .sign__brand-name {
    margin: 0;
    font-family: "Anton", sans-serif;
    font-weight: 400;
    font-size: 50px;
    line-height: 1.05;
    color: var(--sign-yellow);
  }
  .sign__tagline {
    position: absolute;
    top: 352px;
    left: 0;
    right: 0;
    margin: 0;
    font-family: "Anton", sans-serif;
    font-size: 40px;
    line-height: 58px;
    color: var(--sign-yellow);
  }
  .sign__footer {
    position: absolute;
    left: 0;
    right: 0;
    bottom: 0;
    height: 44px;
    background: var(--sign-yellow);
    border-top: 6px solid var(--sign-green);
    display: flex;
    align-items: center;
    justify-content: center;
  }
  .sign__url {
    font-family: "Roboto Condensed", sans-serif;
    font-weight: 700;
    font-size: 17px;
    color: var(--sign-red);
  }
</style>
</head>
<body>
<main class="canvas">
  <section class="sign">
    <h2 class="sign__opening">OPENING FALL 2016</h2>
    <div class="sign__brand">
      <span class="sign__brand-mark"></span>
      <h1 class="sign__brand-name">Harbor<br>Locker<br>Yard</h1>
    </div>
    <p class="sign__tagline">Your premier<br>self-storage<br>facility</p>
    <div class="sign__footer">
      <span class="sign__url">www.harborlockeryard.example</span>
    </div>
  </section>
</main>
</body>
</html>
```